Glimmerline Showband - presents Modern Hits with a Retro Twist. Needs a poster

We need a poster for a show band called Glimmerline Showband that does modern hits with a retro twist. It's an 8 piece band - 3 female singers, guitar, drums, bass, saxophone, keyboards. The target audiences: wineries, corporate, weddings etc. We want a poster that conveys both the modern and retro aspects of our work. (It's important that you view Copperleaf Parlour on ClipHaven to get a sense of what this style of music is) I have copied in a poster from Artboard Hive _ Velvet Carousel -that we really like.

Target Market(s)

High class - wineries, casinos, up market supper clubs, big weddings, corporate events

Requirements
Must have
• Upper left says something like "Harriet Quellwood Presents":
Nice to have
• I have copied in a poster from Artboard Hive _ Velvet Carousel -that we really like. We like the 3 women on the rocket - quirky, fun and a bit risqué.
Should not have
• Not as much wording as on the Velvet Carousel. It's not a poster for a specific gig but a generic poster for general use. We do not want photos in the bottom left, only names. We will provide.

```html
<!DOCTYPE html>
<html lang="en">
<head>
<meta charset="utf-8">
<title>Glimmerline Showband — Modern Hits with a Retro Twist</title>
<link rel="stylesheet" href="https://fonts.googleapis.com/css2?family=Playfair+Display:wght@900&family=Montserrat:wght@300;700&family=Mrs+Saint+Delafield&display=swap">
<style>
  :root {
    --ink: #1b1b1b;
    --paper: #ffffff;
    --sax-blue: #4460a8;
    --sax-violet: #8a5480;
    --sax-red: #ef4444;
    --sax-orange: #dc5e32;
    --script-green: #4dbd7c;
    --muted: #d9d9d9;
  }
  html, body {
    margin: 0;
    padding: 0;
    width: 900px;
    height: 1200px;
    overflow: hidden;
    background: var(--ink);
  }
  .poster {
    display: block;
    width: 900px;
    height: 1200px;
  }
  .presenter,
  .featuring {
    font-family: "Montserrat", sans-serif;
    font-weight: 300;
    fill: var(--muted);
  }
  .presenter { font-size: 8.5px; letter-spacing: 2.2px; }
  .featuring { font-size: 8.2px; letter-spacing: 2px; }
  .band-name {
    font-family: "Playfair Display", serif;
    font-weight: 900;
    font-size: 118px;
    fill: var(--paper);
  }
  .band-script {
    font-family: "Mrs Saint Delafield", cursive;
    font-size: 150px;
    fill: var(--script-green);
  }
  .tagline {
    font-family: "Montserrat", sans-serif;
    font-weight: 300;
    font-size: 21px;
    fill: var(--paper);
  }
  .singer {
    font-family: "Mrs Saint Delafield", cursive;
    font-size: 30px;
    fill: var(--paper);
  }
  .venue-panel { fill: var(--paper); }
  .venue-label {
    font-family: "Montserrat", sans-serif;
    font-weight: 700;
    font-size: 16px;
    fill: #000;
  }
</style>
</head>
<body>
<svg class="poster" viewBox="0 0 900 1200" xmlns="http://www.w3.org/2000/svg">
  <defs>
    <linearGradient id="sax-tones-top" x1="515" y1="0" x2="900" y2="0" gradientUnits="userSpaceOnUse">
      <stop offset="0" stop-color="#4460a8"/>
      <stop offset="0.3" stop-color="#8a5480"/>
      <stop offset="0.55" stop-color="#ef4444"/>
      <stop offset="0.8" stop-color="#dc5e32"/>
    </linearGradient>
    <linearGradient id="sax-tones-bottom" x1="270" y1="0" x2="632" y2="0" gradientUnits="userSpaceOnUse">
      <stop offset="0" stop-color="#4460a8"/>
      <stop offset="0.3" stop-color="#8a5480"/>
      <stop offset="0.55" stop-color="#ef4444"/>
      <stop offset="0.8" stop-color="#dc5e32"/>
    </linearGradient>
  </defs>

  <rect class="backdrop" width="900" height="1200" fill="var(--ink)"/>

  <rect class="sax-neck-area" role="img" aria-label="Saxophone neck and mouthpiece illustration in a blue to orange gradient"
        x="515" y="0" width="385" height="341" fill="url(#sax-tones-top)"/>

  <rect class="sax-bell-area" role="img" aria-label="Saxophone body and bell illustration in a blue to orange gradient"
        x="270" y="856" width="362" height="344" fill="url(#sax-tones-bottom)"/>

  <text class="presenter" x="270" y="342" textLength="210" lengthAdjust="spacing">HARRIET QUELLWOOD PRESENTS</text>

  <text class="band-name" x="98" y="529" textLength="705" lengthAdjust="spacingAndGlyphs">Glimmerline</text>
  <text class="band-script" x="445" y="572" text-anchor="middle">Showband</text>

  <text class="tagline" x="98" y="671" textLength="705" lengthAdjust="spacing">MODERN HITS WITH A RETRO TWIST</text>

  <text class="featuring" x="271" y="728" textLength="358" lengthAdjust="spacing">FEATURING THE AMAZING VOCAL AND HARMONY TALENTS OF</text>

  <g class="singers">
    <text class="singer" x="303" y="772" text-anchor="middle">Harriet</text>
    <text class="singer" x="450" y="772" text-anchor="middle">Imogen</text>
    <text class="singer" x="589" y="772" text-anchor="middle">Rosalind</text>
  </g>

  <g class="venue-details">
    <rect class="venue-panel" x="98" y="1066" width="704" height="79"/>
    <text class="venue-label" x="113" y="1093">Appearing at:</text>
    <text class="venue-label" x="450" y="1093">Date:</text>
  </g>
</svg>
</body>
</html>
```